Fitness competition business needs a card design

I need a professional business card design using my logo. The card will be horizontal with rounded edges.

Target Market(s)

Female fitness competitors

Industry/Entity Type

Fitness

Contact Information for Business Card

Rose-Lynn Darby
Owner
stagevarno.com
555.301.2187
info@stagevarno.com

Font styles to use
Serif

Colors

Designer to choose colors to be used in the design.

Requirements
Must have
• On the back please add the following:
• Figure
• Bikini
• Physique
• Fitness
Nice to have
• Looking for a very sleek design, contemporary and easy to read.
Should not have
• Should not be difficult to read or be too busy

```html
<!DOCTYPE html>
<html lang="en">
<head>
<meta charset="utf-8">
<title>Stage Varno – Business Card</title>
<link rel="stylesheet" href="https://fonts.googleapis.com/css2?family=Lato:wght@300;400;700&display=swap">
<style>
  :root {
    --backdrop: #4b4a72;
    --card: #ffffff;
    --brand-red: #e8262b;
    --ink: #555555;
    --ink-soft: #777777;
    --rule: #5a5a5a;
  }
  * { margin: 0; padding: 0; box-sizing: border-box; }
  html, body {
    width: 1200px; height: 1000px; overflow: hidden;
    background: var(--backdrop);
    font-family: "Lato", sans-serif;
  }
  .card {
    position: absolute; left: 278px; width: 642px; height: 366px;
    background: var(--card); border-radius: 36px; overflow: hidden;
  }
  .card--front { top: 98px; }
  .card--back { top: 528px; }

  .brand {
    position: absolute; display: flex; align-items: center;
    color: var(--brand-red); font-weight: 700; letter-spacing: 0.04em;
    white-space: nowrap;
  }
  .brand__dot { background: var(--brand-red); border-radius: 50%; flex: none; }
  .card--front .brand {
    left: 0; right: 0; top: 150px; justify-content: center; gap: 18px; font-size: 46px;
  }
  .card--front .brand__dot { width: 22px; height: 22px; }
  .card--back .brand {
    right: 54px; top: 86px; gap: 10px; font-size: 24px;
  }
  .card--back .brand__dot { width: 12px; height: 12px; }

  .disciplines {
    position: absolute; left: 0; right: 0; top: 311px;
    display: flex; justify-content: center; align-items: center;
    font-weight: 300; font-size: 22px; color: var(--ink-soft);
  }
  .disciplines__sep {
    display: inline-block; width: 2px; height: 26px;
    background: var(--brand-red); margin: 0 8px;
  }

  .holder { position: absolute; left: 35px; top: 104px; color: var(--ink); }
  .holder__name { font-size: 29px; font-weight: 400; line-height: 1.1; }
  .holder__role { font-size: 18px; margin-top: 6px; }
  .divider {
    position: absolute; left: 37px; width: 571px; top: 179px;
    height: 2px; background: var(--rule);
  }
  .contact { position: absolute; left: 34px; top: 220px; list-style: none; color: var(--ink); }
  .contact__item {
    display: flex; align-items: center; gap: 20px;
    font-size: 22px; letter-spacing: 0.02em; height: 35px;
  }
  .contact__icon { width: 21px; height: 21px; fill: var(--ink); flex: none; }

  .web-tab { position: absolute; right: 0; bottom: 0; width: 310px; height: 56px; }
  .web-tab svg { position: absolute; inset: 0; }
  .web-tab__text {
    position: absolute; left: 47px; top: 13px;
    color: #fff; font-size: 18px; letter-spacing: 0.02em;
  }
</style>
</head>
<body>
  <section class="card card--front">
    <div class="brand"><span class="brand__dot"></span>STAGE VARNO</div>
    <p class="disciplines">
      <span>Figure</span><span class="disciplines__sep"></span>
      <span>Bikini</span><span class="disciplines__sep"></span>
      <span>Physique</span><span class="disciplines__sep"></span>
      <span>Fitness</span>
    </p>
  </section>

  <section class="card card--back">
    <div class="brand"><span class="brand__dot"></span>STAGE VARNO</div>
    <div class="holder">
      <h1 class="holder__name">Rose-Lynn Darby</h1>
      <p class="holder__role">Owner</p>
    </div>
    <div class="divider"></div>
    <ul class="contact">
      <li class="contact__item">
        <svg class="contact__icon" viewBox="0 0 24 24" aria-hidden="true"><path d="M6.6 10.8c1.4 2.8 3.8 5.1 6.6 6.6l2.2-2.2c.3-.3.7-.4 1-.2 1.1.4 2.3.6 3.6.6.6 0 1 .4 1 1V20c0 .6-.4 1-1 1C10.6 21 3 13.4 3 4c0-.6.4-1 1-1h3.5c.6 0 1 .4 1 1 0 1.3.2 2.5.6 3.6.1.3 0 .7-.2 1z"/></svg>
        <span>555.301.2187</span>
      </li>
      <li class="contact__item">
        <svg class="contact__icon" viewBox="0 0 24 24" aria-hidden="true"><path d="M2 6h20v12H2z M2 6l10 7 10-7" fill="none" stroke="#555" stroke-width="0"/><path d="M2 7.5V18h20V7.5l-10 7z"/><path d="M2.5 6h19L12 12.5z"/></svg>
        <span>info@stagevarno.com</span>
      </li>
    </ul>
    <div class="web-tab">
      <svg viewBox="0 0 310 56" preserveAspectRatio="none" aria-hidden="true">
        <path d="M0 56 L18 8 Q21 0 32 0 H310 V56 Z" fill="#e8262b"/>
      </svg>
      <span class="web-tab__text">www.stagevarno.com</span>
    </div>
  </section>
</body>
</html>
```